8.5 x 8.5 - HELOC Product Campaign

Home Equity Lines of Credit
are BACK!!!

* Up to 97.5% on Owner Occupied Properties
* 700 Minimum Scores
* Fund in only 2-3 weeks

Can be used for...
* Education Expense
* Bill Consolidation
* Home Improvement
* Investments

Call today for more information!
(800) 417-2960

Bluegate Lending Partners, Inc.
NMLS #381760
www.bluegatelendhub.com

```html
<!DOCTYPE html>
<html lang="en">
<head>
<meta charset="UTF-8">
<title>HELOC Product Campaign – Bluegate Lending Partners</title>
<link href="https://fonts.googleapis.com/css2?family=Fira+Sans:wght@500;600;700&family=Montserrat:wght@500;600&display=swap" rel="stylesheet">
<style>
  :root{
    --navy:#23478f;
    --blue:#2b5aa6;
    --blue-deep:#1d3e80;
    --gold:#a39535;
    --gold-text:#a8983a;
    --white:#ffffff;
    --panel:#e9eef6;
    --ink:#1b2a4a;
    --grey:#b5b5b5;
  }
  *{box-sizing:border-box;margin:0;padding:0}
  html,body{width:1200px;height:1200px;overflow:hidden;background:#ffffff}
  body{font-family:"Fira Sans",Arial,sans-serif}
  .flyer{position:relative;width:1200px;height:1200px;background:var(--white)}

  .hero{position:absolute;left:34px;top:34px;width:1132px;height:688px;
        background:linear-gradient(180deg,var(--blue) 0%,var(--navy) 100%);overflow:hidden}
  .hero-photo{position:absolute;right:0;top:0;width:420px;height:688px;
        background:radial-gradient(ellipse at 50% 45%,#6b4a3a 0%,#2a2438 45%,rgba(35,71,143,0) 75%)}
  .headline{position:absolute;left:48px;top:112px;color:var(--white);font-weight:600;font-size:41px;letter-spacing:.3px}
  .back{position:absolute;left:40px;top:150px;font-family:"Montserrat",Arial,sans-serif;font-weight:500;
        font-size:196px;line-height:1;color:var(--gold-text);letter-spacing:-2px}

  .perks{position:absolute;left:48px;top:392px;width:690px;height:212px;background:var(--panel);
         border-radius:6px;padding:20px 40px 0 36px;list-style:none}
  .perks li{display:flex;align-items:center;gap:22px;height:62px;border-bottom:1.5px solid var(--blue);
            color:var(--ink);font-weight:600;font-size:27px}
  .perks li:last-child{border-bottom:none}
  .perks .big{font-size:36px;font-weight:700;margin-right:6px}
  .tick{flex:none;width:22px;height:22px}

  .divider{position:absolute;left:34px;top:722px;width:1132px;height:6px;background:var(--white)}
  .uses{position:absolute;left:34px;top:728px;width:1132px;height:200px;background:var(--gold);border-top:5px solid var(--blue)}
  .uses-tab{position:absolute;left:50%;transform:translateX(-50%);top:-5px;width:360px;height:54px;
            background:var(--blue);color:var(--white);border-radius:0 0 10px 10px;
            font-family:"Montserrat",Arial,sans-serif;font-weight:500;font-size:29px;
            display:flex;align-items:center;justify-content:center;letter-spacing:.5px}
  .uses-list{position:absolute;left:0;top:60px;width:100%;height:130px;display:flex;list-style:none}
  .uses-list li{flex:1;display:flex;flex-direction:column;align-items:center;justify-content:flex-end;gap:18px;
                color:var(--white);font-weight:600;font-size:24px;padding-bottom:18px;
                border-right:2px dashed rgba(255,255,255,.7)}
  .uses-list li:last-child{border-right:none}
  .use-icon{width:64px;height:64px}

  .footer{position:absolute;left:34px;top:928px;width:1132px;height:222px}
  .brand{position:absolute;left:36px;top:50px;width:380px;text-align:center}
  .brand-name{display:flex;align-items:center;justify-content:center;gap:10px;color:var(--blue);
              font-weight:700;font-size:21px;line-height:1.2;white-space:nowrap}
  .brand-mark{flex:none;width:22px;height:22px;border-radius:50%;background:var(--gold)}
  .nmls{margin-top:40px;color:var(--blue);font-weight:500;font-size:26px;letter-spacing:.5px}
  .cta{position:absolute;right:36px;top:22px;width:660px}
  .cta-title{font-family:"Montserrat",Arial,sans-serif;font-weight:500;font-size:27px;line-height:1.2;color:var(--blue);
             border-bottom:2px solid var(--grey);padding-bottom:6px;text-align:right;white-space:nowrap}
  .contact{display:flex;align-items:center;justify-content:flex-end;gap:24px;margin-top:10px}
  .contact svg{flex:none;width:40px;height:40px}
  .phone{font-family:"Montserrat",Arial,sans-serif;font-weight:600;font-size:60px;line-height:1.1;color:var(--gold-text);white-space:nowrap}
  .web{font-weight:700;font-size:30px;line-height:1.2;color:var(--gold-text);letter-spacing:3px;white-space:nowrap}
  .web .host{color:var(--blue)}
  .base-bar{position:absolute;left:34px;top:1152px;width:1132px;height:14px;background:var(--grey)}
</style>
</head>
<body>
<main class="flyer">
  <section class="hero">
    <div class="hero-photo" role="img" aria-label="Photo of a smiling graduate in cap and dark off-shoulder top"></div>
    <h1 class="headline">Home Equity Lines of Credit are</h1>
    <p class="back">BACK!!!</p>
    <ul class="perks">
      <li><svg class="tick" viewBox="0 0 22 22"><circle cx="11" cy="11" r="11" fill="#2b5aa6"/><path d="M6 11.5l3.3 3.2L16 8" fill="none" stroke="#fff" stroke-width="2.4"/></svg><span>Up to <span class="big">97.5%</span>on Owner Occupied Properties</span></li>
      <li><svg class="tick" viewBox="0 0 22 22"><circle cx="11" cy="11" r="11" fill="#2b5aa6"/><path d="M6 11.5l3.3 3.2L16 8" fill="none" stroke="#fff" stroke-width="2.4"/></svg><span><span class="big">700</span>Minimum Scores</span></li>
      <li><svg class="tick" viewBox="0 0 22 22"><circle cx="11" cy="11" r="11" fill="#2b5aa6"/><path d="M6 11.5l3.3 3.2L16 8" fill="none" stroke="#fff" stroke-width="2.4"/></svg><span>Fund in only <span class="big">2-3 weeks</span></span></li>
    </ul>
  </section>

  <div class="divider"></div>
  <section class="uses">
    <div class="uses-tab">CAN BE USED FOR</div>
    <ul class="uses-list">
      <li>
        <svg class="use-icon" viewBox="0 0 64 64"><circle cx="32" cy="32" r="32" fill="#fff"/><rect x="16" y="38" width="32" height="7" rx="2" fill="#2b5aa6"/><rect x="18" y="30" width="28" height="7" rx="2" fill="#2b5aa6"/><path d="M32 14l16 6-16 6-16-6z" fill="#2b5aa6"/><path d="M24 23v5h16v-5" fill="#2b5aa6"/></svg>
        Education Expense
      </li>
      <li>
        <svg class="use-icon" viewBox="0 0 64 64"><circle cx="32" cy="32" r="32" fill="#fff"/><path d="M20 14h24v36l-4-3-4 3-4-3-4 3-4-3-4 3z" fill="#2b5aa6"/><path d="M25 30h14M25 36h14M25 42h10" stroke="#fff" stroke-width="2"/><text x="32" y="25" text-anchor="middle" font-size="10" fill="#fff" font-family="Arial">$</text></svg>
        Bill Consolidation
      </li>
      <li>
        <svg class="use-icon" viewBox="0 0 64 64"><circle cx="32" cy="32" r="32" fill="#fff"/><path d="M12 33L32 16l20 17-3 3-17-14-17 14z" fill="#2b5aa6"/><path d="M19 34l13-11 13 11v14H37v-9h-10v9h-8z" fill="#2b5aa6"/></svg>
        Home Improvement
      </li>
      <li>
        <svg class="use-icon" viewBox="0 0 64 64"><circle cx="32" cy="32" r="32" fill="#fff"/><path d="M26 14h12l-4 8h-4z" fill="#2b5aa6"/><path d="M29 22h6c9 6 13 13 13 19 0 6-5 9-16 9s-16-3-16-9c0-6 4-13 13-19z" fill="#2b5aa6"/><text x="32" y="44" text-anchor="middle" font-size="16" font-weight="bold" fill="#fff" font-family="Arial">$</text></svg>
        Investments
      </li>
    </ul>
  </section>

  <footer class="footer">
    <div class="brand">
      <p class="brand-name"><span class="brand-mark"></span>Bluegate Lending Partners, Inc.</p>
      <p class="nmls">NMLS #381760</p>
    </div>
    <div class="cta">
      <p class="cta-title">CALL TODAY FOR MORE INFORMATION!</p>
      <p class="contact">
        <svg viewBox="0 0 42 42"><path d="M10 6l7 7-4 5c2 5 6 9 11 11l5-4 7 7-5 5C18 37 5 24 5 11z" fill="#2b5aa6"/></svg>
        <span class="phone">(800) 417-2960</span>
      </p>
      <p class="contact">
        <svg viewBox="0 0 42 42"><circle cx="21" cy="21" r="17" fill="none" stroke="#2b5aa6" stroke-width="3"/><ellipse cx="21" cy="21" rx="7" ry="17" fill="none" stroke="#2b5aa6" stroke-width="2.5"/><path d="M4 21h34M7 12h28M7 30h28" stroke="#2b5aa6" stroke-width="2.5"/></svg>
        <span class="web">www.<span class="host">bluegatelendhub</span>.com</span>
      </p>
    </div>
  </footer>
  <div class="base-bar"></div>
</main>
</body>
</html>
```